Business Card Design Project

We need a business card design for a consultancy called 'Amber Ridge'. The design should communicate innovation and professionalism. The colors used should complement our logo. Please include source files for winning design.
Updates

Industry/Entity Type

Business

Colors

Designer to choose colors to be used in the design.

Requirements
Must have
• Card size should be 85mm x 50mm. The back side of the card should be the logo on a black background. The front side should display the name 'Amber Ridge' along with standard information. The front's design should graphically complement the back.
Nice to have
• Any graphical elements in the front the complement the back side (with the logo on a black background) would be a plus.

```html
<!DOCTYPE html>
<html lang="en">
<head>
<meta charset="utf-8">
<title>Amber Ridge – Business Cards</title>
<link rel="stylesheet" href="https://fonts.googleapis.com/css2?family=Questrial&family=Mulish:wght@800&display=swap">
<style>
  :root {
    --page: #e4e2df;
    --ink: #141414;
    --card-black: #0c0c0c;
    --card-white: #ffffff;
    --amber: #e8943f;
    --amber-deep: #e8893a;
    --beam-start: #ff9a55;
    --beam-end: #f3e6df;
    --body-text: #2a2a2a;
  }
  * { box-sizing: border-box; margin: 0; padding: 0; }
  html, body { width: 1200px; height: 871px; overflow: hidden; }
  body { background: var(--page); position: relative; font-family: "Questrial", sans-serif; }

  .card {
    position: absolute;
    width: 620px;
    height: 365px;
    border-radius: 4px;
    overflow: hidden;
    box-shadow: 0 10px 24px rgba(0,0,0,0.18);
  }

  /* Back side */
  .card-back { left: 70px; top: 50px; background: var(--card-black); }
  .brand {
    position: absolute; inset: 0;
    display: flex; align-items: center; justify-content: center;
    gap: 16px;
  }
  .brand-dot {
    width: 22px; height: 22px; border-radius: 50%;
    background: var(--amber);
  }
  .brand-name {
    font-family: "Questrial", sans-serif; font-weight: 400;
    font-size: 42px; color: var(--amber);
  }

  /* Front side */
  .card-front { left: 510px; top: 456px; background: var(--card-white); }
  .card-front svg.art { position: absolute; inset: 0; }

  .contact {
    position: absolute; right: 34px; top: 112px;
    text-align: right; color: var(--body-text);
  }
  .contact-name { font-family: "Mulish", sans-serif; font-weight: 800; font-size: 19px; color: var(--ink); }
  .contact-role { font-size: 15px; color: var(--amber-deep); margin-bottom: 12px; }
  .contact-address { font-size: 16px; line-height: 22px; margin-bottom: 10px; }
  .contact-lines { list-style: none; font-size: 16px; line-height: 24px; }
  .contact-lines li { display: flex; justify-content: flex-end; align-items: center; gap: 10px; }
  .contact-lines svg { width: 14px; height: 14px; fill: var(--amber-deep); flex: none; }
</style>
</head>
<body>

  <section class="card card-back" aria-label="Card back">
    <div class="brand">
      <div class="brand-dot"></div>
      <div class="brand-name">Amber Ridge</div>
    </div>
  </section>

  <section class="card card-front" aria-label="Card front">
    <svg class="art" viewBox="0 0 620 365" width="620" height="365">
      <defs>
        <linearGradient id="beam" x1="0" y1="0" x2="1" y2="0.3">
          <stop offset="0" stop-color="var(--beam-start)"/>
          <stop offset="1" stop-color="var(--beam-end)"/>
        </linearGradient>
      </defs>
      <polygon class="light-beam" points="248,78 620,18 620,365 420,365" fill="url(#beam)"/>
      <rect class="illustration" role="img" aria-label="Black lighthouse silhouette on a rocky shore"
            x="0" y="60" width="260" height="240" fill="var(--ink)"/>
    </svg>

    <div class="contact">
      <div class="contact-name">Mara Ellison</div>
      <div class="contact-role">Ceo</div>
      <div class="contact-address">Level 3, 210 Harbour Road<br>NSW 2071</div>
      <ul class="contact-lines">
        <li>02 9612 0374
          <svg viewBox="0 0 16 16" aria-hidden="true"><path d="M3 2h3l1 4-2 1a9 9 0 0 0 4 4l1-2 4 1v3a1 1 0 0 1-1 1A13 13 0 0 1 2 3a1 1 0 0 1 1-1z"/></svg>
        </li>
        <li>02 961 0375
          <svg viewBox="0 0 16 16" aria-hidden="true"><path d="M4 1h8v4H4zM1 6h14v6h-3v3H4v-3H1zM5 10v4h6v-4z"/></svg>
        </li>
        <li>enquiries@amberridge.com
          <svg viewBox="0 0 16 16" aria-hidden="true"><path d="M1 3h14v10H1zM2 4.5v.3l6 4 6-4v-.3z"/></svg>
        </li>
      </ul>
    </div>
  </section>

</body>
</html>
```